Tall Fern Software PowerPoint template

We are a software company selling endpoint visibility, access and security technology to enterprise-level IT departments.
Our technology helps organizations gain comprehensive visibility into and control over devices accessing their corporate network so they can quickly identify and address suspicious activity on the network that could lead to potential threats like data breaches.
This technology can cost organizations upwards of $1M - depending on the size of the organization. Our primary clients are Marquee 3,000 companies.
We want a professional, polished PowerPoint template that we can use for all company presentations. Please include:
Title page
Section page
General info page
Thank you page
Logo options and color specs are attached.
Please include our tagline on at least the title page: Chart the frontier. Steady the core.
Software

```html
<!DOCTYPE html>
<html lang="en">
<head>
<meta charset="utf-8">
<title>Tall Fern Software — Title Slide</title>
<link href="https://fonts.googleapis.com/css2?family=Roboto:wght@400;500&display=swap" rel="stylesheet">
<style>
  :root {
    --brand-red: #951c18;
    --brand-maroon: #5c0c09;
    --brand-tan: #d58a69;
    --text-light: #f6e9e7;
    --paper: #ffffff;
    --footer-grey: #58585a;
  }
  * { margin: 0; padding: 0; box-sizing: border-box; }
  html, body { width: 1200px; height: 900px; overflow: hidden; background: var(--paper); }
  .slide {
    position: relative;
    width: 1200px;
    height: 900px;
    font-family: "Roboto", Arial, sans-serif;
    background: var(--paper);
  }
  .hero {
    position: absolute;
    inset: 0 0 auto 0;
    height: 612px;
    background: var(--brand-red);
  }
  .hero-art {
    position: absolute;
    left: 0;
    top: 0;
    width: 620px;
    height: 612px;
    background: radial-gradient(circle at 305px 304px, rgba(255,255,255,0.12) 0, rgba(255,255,255,0.05) 170px, rgba(255,255,255,0) 300px);
  }
  .hero-copy {
    position: absolute;
    right: 45px;
    top: 282px;
    text-align: right;
  }
  .tagline-line {
    font-weight: 500;
    font-size: 39px;
    line-height: 60px;
    letter-spacing: 0.2px;
    text-transform: uppercase;
  }
  .tagline-line--primary { color: var(--brand-maroon); }
  .tagline-line--accent { color: var(--brand-tan); }
  .subtext {
    margin-top: 26px;
    width: 470px;
    margin-left: auto;
    color: var(--text-light);
    font-size: 20px;
    line-height: 31px;
  }
  .brand-mark {
    position: absolute;
    right: 50px;
    top: 700px;
    display: flex;
    align-items: center;
    gap: 22px;
  }
  .brand-dot {
    width: 34px;
    height: 34px;
    border-radius: 50%;
    background: var(--brand-red);
  }
  .brand-name {
    font-weight: 500;
    font-size: 40px;
    letter-spacing: 2px;
    color: var(--brand-red);
  }
  .footer-band {
    position: absolute;
    left: 0;
    right: 0;
    bottom: 0;
    height: 42px;
    background: var(--footer-grey);
  }
</style>
</head>
<body>
  <main class="slide">
    <section class="hero">
      <div class="hero-art" role="img" aria-label="Decorative brand pattern area"></div>
      <div class="hero-copy">
        <h1 class="tagline-line tagline-line--primary">Chart the frontier</h1>
        <h2 class="tagline-line tagline-line--accent">Steady the core</h2>
        <p class="subtext">Subtext here Subtext here Subtext here Subtext here Subtext here Subtext here</p>
      </div>
    </section>
    <div class="brand-mark">
      <span class="brand-dot"></span>
      <span class="brand-name">Tall Fern Software</span>
    </div>
    <footer class="footer-band"></footer>
  </main>
</body>
</html>
```